New, modern business card for growing audiology practice

We need a new business card for our audiology practice. Our logo and website have recently changed (more modern) and we want our business cards to reflect this change.
We conduct hearing tests, perform earwax removals, and fit & dispense hearing aids to our patients. We are a family owned practice in which the owner is the one who works directly with the patient. I have attached logos in various formats to use, as well as two ideas I found on this website; as well as a scanned copy of our current logo. Good luck!

Industry/Entity Type

Business

Contact Information for Business Card

Company name: Maplow Hearing Center
Provider name: Peter Mulvoy, Au.D. F/ISN
Phone number: (555) 318-6042
Address: 87 W. Linden Ave. Hollis Bend, ST 00917
email: maplowhearing@postvale.net
website: maplowhearing.com

Colors
000000
aaaaaa
dbdbdb
cacaca
9bcb3c
afd23c
cadf82
b1b1b1

Requirements
Must have
• My card must include information in the "details" section. In the attached images, I found a few that I liked and I would like to model after - "brisk tumblin'" and "Sound Wellness Center".
• Must be horizontal.
• Must include logos provided. I uploaded them in various file formats and various ways.
• Must match logo font, if possible, if not, please get as close as you can.
Nice to have
• I really like the idea of having a color on one side with just the logo and company name and the contact information and provider name on the other side. I also really like the idea of having the main color dominating on the logo/company side with accent of that same color on the contact side of the card.
Should not have
• Must not be vertical.

```html
<!DOCTYPE html>
<html lang="en">
<head>
<meta charset="utf-8">
<title>Maplow Hearing Center – Business Card</title>
<link href="https://fonts.googleapis.com/css2?family=Montserrat:wght@400;500;700&display=swap" rel="stylesheet">
<style>
  :root {
    --ink: #000000;
    --paper: #ffffff;
    --green: #7aa83c;
    --border: #aaaaaa;
    --text: #1a1a1a;
  }
  html, body {
    margin: 0;
    padding: 0;
    width: 1200px;
    height: 1000px;
    overflow: hidden;
    background: var(--paper);
    font-family: "Montserrat", Arial, sans-serif;
  }
  .canvas { position: relative; width: 1200px; height: 1000px; }

  .card { position: absolute; box-sizing: border-box; }

  .card-front {
    left: 345px; top: 186px; width: 511px; height: 307px;
    background: var(--ink);
    display: flex; align-items: center; justify-content: center;
  }
  .brand { display: flex; align-items: center; gap: 12px; margin-top: 12px; }
  .brand-dot {
    width: 28px; height: 28px; border-radius: 50%;
    background: var(--green);
  }
  .brand-name {
    color: var(--paper);
    font-size: 25px; font-weight: 400;
    letter-spacing: 0.2px;
    text-transform: uppercase;
    white-space: nowrap;
  }

  .card-back {
    left: 344px; top: 507px; width: 511px; height: 307px;
    background: var(--paper);
    border: 1px solid var(--border);
  }
  .back-mark {
    position: absolute; left: 46px; top: 92px;
    width: 88px; height: 88px; border-radius: 50%;
    background: var(--green);
  }
  .divider {
    position: absolute; left: 160px; top: 87px;
    width: 2px; height: 129px; background: var(--green);
  }
  .details { position: absolute; left: 186px; top: 102px; }
  .provider {
    margin: 0 0 0 20px;
    font-size: 16px; font-weight: 700; color: var(--ink);
    line-height: 20px;
  }
  .provider .credentials { font-size: 14px; }
  .contact-list { list-style: none; margin: 0; padding: 0; }
  .contact-list li {
    position: relative; padding-left: 20px;
    font-size: 15.5px; line-height: 19.3px; color: var(--text);
    white-space: nowrap;
  }
  .contact-list svg {
    position: absolute; left: 0; top: 3px; width: 13px; height: 13px;
    fill: var(--green);
  }
</style>
</head>
<body>
<main class="canvas">
  <section class="card card-front" aria-label="Card front">
    <div class="brand">
      <span class="brand-dot"></span>
      <span class="brand-name">Maplow Hearing Center</span>
    </div>
  </section>

  <section class="card card-back" aria-label="Card back">
    <span class="back-mark"></span>
    <span class="divider"></span>
    <div class="details">
      <p class="provider">Peter Mulvoy, <span class="credentials">Au.D. F/ISN</span></p>
      <ul class="contact-list">
        <li>
          <svg viewBox="0 0 12 12"><rect x="3" y="1" width="6" height="11" rx="1"/><rect x="4.5" y="0" width="1" height="2"/><rect x="4" y="3" width="4" height="3" fill="#fff"/></svg>
          (555) 318-6042
        </li>
        <li>
          <svg viewBox="0 0 12 12"><path d="M6 1 0 6h2v5h3V8h2v3h3V6h2z"/></svg>
          87 W. Linden Ave. Hollis Bend,<br>ST 00917
        </li>
        <li>
          <svg viewBox="0 0 12 12"><rect x="0" y="2" width="12" height="8"/><path d="M0 2 6 7 12 2" fill="none" stroke="#fff" stroke-width="1"/></svg>
          maplowhearing@postvale.net
        </li>
        <li>
          <svg viewBox="0 0 12 12"><circle cx="6" cy="6" r="6"/><path d="M0 6h12M6 0v12M6 0C3 3 3 9 6 12M6 0c3 3 3 9 0 12" fill="none" stroke="#fff" stroke-width="0.8"/></svg>
          www.maplowhearing.com
        </li>
      </ul>
    </div>
  </section>
</main>
</body>
</html>
```